Business Card Design Project

We would need a business name card for our online website business, http://www.brindle.com.sg/. We would need to include our website on the name card as well.

Target Market(s)

Adults and kids in Singapore, mainly expatriates

Industry/Entity Type

Business

Font styles to use
Sans Serif

Colors

Designer to choose colors to be used in the design.

Requirements
Must have
• Must include our "vorn" logo and we would like our name card to be printed on light craft paper material

```html
<!DOCTYPE html>
<html lang="en">
<head>
<meta charset="utf-8">
<title>Vorn Business Card</title>
<link href="https://fonts.googleapis.com/css2?family=Open+Sans:wght@400;600;700&display=swap" rel="stylesheet">
<style>
  :root {
    --navy: #232c80;
    --red: #d3211f;
    --paper: #ffffff;
    --backdrop: #e9e6e1;
    --ink-soft: #333333;
    --on-navy: #ffffff;
  }
  * { box-sizing: border-box; margin: 0; padding: 0; }
  html, body { width: 1200px; height: 768px; overflow: hidden; }
  body {
    background: var(--backdrop);
    font-family: "Open Sans", Arial, sans-serif;
    display: flex;
    align-items: center;
    justify-content: center;
    gap: 60px;
  }
  .card {
    position: relative;
    width: 525px;
    height: 300px;
    background: var(--paper);
    overflow: hidden;
    box-shadow: 0 6px 18px rgba(0,0,0,0.18);
  }
  .brand {
    position: absolute;
    display: flex;
    align-items: center;
    gap: 12px;
  }
  .brand-dot {
    width: 34px; height: 34px;
    border-radius: 50%;
    background: var(--red);
  }
  .brand-name {
    font-weight: 700;
    font-size: 40px;
    letter-spacing: 3px;
    color: var(--navy);
  }
  /* front */
  .card-front .brand { left: 50%; top: 62px; transform: translateX(-50%); }
  .rule {
    position: absolute;
    left: 60px; right: 60px;
    height: 1px;
    background: var(--navy);
  }
  .rule-top { top: 168px; }
  .rule-bottom { top: 238px; }
  .front-site {
    position: absolute;
    left: 70px; top: 190px;
    font-size: 15px;
    font-weight: 600;
    color: var(--red);
  }
  /* back */
  .card-back .brand { left: 48px; top: 60px; }
  .waves { position: absolute; inset: 0; width: 100%; height: 100%; }
  .person {
    position: absolute;
    right: 24px; top: 92px;
    text-align: right;
  }
  .person-name { font-size: 21px; font-weight: 600; color: var(--navy); line-height: 28px; }
  .person-title { font-size: 12px; color: var(--ink-soft); margin-top: 2px; }
  .contacts {
    position: absolute;
    right: 22px; bottom: 10px;
    list-style: none;
    color: var(--on-navy);
    font-size: 15px;
    line-height: 21px;
    text-align: right;
  }
  .contacts li { display: flex; align-items: center; justify-content: flex-end; gap: 8px; }
  .contacts svg { width: 12px; height: 12px; fill: var(--red); flex: none; }
</style>
</head>
<body>
  <section class="card card-front">
    <div class="brand"><span class="brand-dot"></span><span class="brand-name">VORN</span></div>
    <div class="rule rule-top"></div>
    <p class="front-site">www.vornhaus.com</p>
    <div class="rule rule-bottom"></div>
  </section>

  <section class="card card-back">
    <svg class="waves" viewBox="0 0 525 300" preserveAspectRatio="none" aria-hidden="true">
      <path d="M0,140 C120,190 280,185 525,160 L525,168 C280,195 120,200 0,152 Z" fill="var(--red)"/>
      <path d="M0,160 C130,205 290,198 525,172 L525,176 C290,204 130,212 0,168 Z" fill="var(--red)"/>
      <path d="M0,178 C140,228 300,214 525,182 L525,300 L0,300 Z" fill="var(--navy)"/>
    </svg>
    <div class="brand"><span class="brand-dot"></span><span class="brand-name">VORN</span></div>
    <div class="person">
      <p class="person-name">Your Long Name</p>
      <p class="person-title">Your Title</p>
    </div>
    <ul class="contacts">
      <li>(+65) 60481230 <svg viewBox="0 0 12 12"><path d="M2 1h3l1 3-2 1a7 7 0 0 0 3 3l1-2 3 1v3c-6 0-10-4-10-10z"/></svg></li>
      <li>(+65) 60481237 <svg viewBox="0 0 12 12"><path d="M3 0h6v4H3zM0 5h12v5H9v2H3v-2H0zM4 8v3h4V8z"/></svg></li>
      <li>www.vornhaus.com <svg viewBox="0 0 12 12"><circle cx="6" cy="6" r="6"/></svg></li>
      <li>hello@vornhaus.com <svg viewBox="0 0 12 12"><path d="M0 2h12v8H0zM1 3l5 4 5-4z"/></svg></li>
    </ul>
  </section>
</body>
</html>
```